Education Foundation Needs a Flyer for an Awareness/Fundraising Event

We need a flyer design for our Education Celebration that is held each year to commemorate Lone Star Learning Days.

This event provides an excellent opportunity for the community to come together to celebrate the education of our children and support the Brookmere Unified Learning District. All twelve schools in the district will have tabletop displays highlighting some of their activities during the year. Teachers will also have grant displays to spotlight the innovative classroom projects they implemented due to funding provided by the Brookmere Learning Trust.

The evening will also include entertainment provided by BULD school choirs. The event concludes with drawing for prices, and a raffle drawing.

Listed below are the details that need to be included in the flyer. I have also included our logo that must be used. I also included some photos from past celebrations that may or may not be helpful.

Please join the Brookmere Learning Trust as we celebrate BULD and its students, educational programs, and schools.

Thursday, March 26, 2015
5:00 p.m. – 8:00 p.m.
Brookmere Senior Academy

Students: Please sign up to be entered in a drawing for Pixora Mini.
Adults: Please sign up to be entered in a drawing for a $50 Shopwell Gift Card.

Raffle Prizes
KORVAN 50" Class 1080p LED Smart HDTV
Zentra Prime Console w/ Motionbar
Donations of $2 each or 3 for $5, or 7 for $10
*Tickets are available at the BULD Administration Building/ Communications and at the schools. (You must be present to win.)

Prizes Galore!
• Campus with the highest percentage of adult attendance will win $300 + the Traveling
Trophy for one year.
• Campus with the 2nd highest percentage of adult attendance will win $150.
• Additional drawings for Teacher, Principal/ Asst. Principal, and District Personnel will be held.

Your Choice – Your Prize
Drawings

7" Dravik NEBULA Pad 4
Fennix Streamlet
Brewlo Classic B20 Single Serve
External Hard Drive
Brewlo 3.0 B700 Coffee Brewing System w/ Carafe
Fennix Streamlet
Cotton Candy Maker
*For your donation of $1.00 per ticket, you may place your ticket(s) in one or all of the baskets. It’s your choice. (You must be present to win.)

Food!
Hot Dogs $1.00
Corn Dogs $0.75
Chips $0.50
Drinks $0.75
Cookies $0.75
Baskets - $2.50 (Hot Dog or Corn Dog, Chips, Drink, Cookie)

For more information, please call 555-318-2946.

```html
<!DOCTYPE html>
<html lang="en">
<head>
<meta charset="utf-8">
<title>Brookmere Learning Trust – Education Celebration</title>
<link href="https://fonts.googleapis.com/css2?family=Oswald:wght@500;600&family=Roboto+Condensed:wght@400;700&family=Open+Sans:wght@400;600&display=swap" rel="stylesheet">
<style>
  :root {
    --royal: #23449a;
    --royal-deep: #1a3580;
    --gold: #f2c21b;
    --sky: #8ec8f0;
    --white: #ffffff;
    --paper: #f1f1f1;
    --paper-shade: #d9d9d9;
    --red: #d4232a;
    --ink: #2a2a2a;
    --label-blue: #1f5aa8;
  }
  * { margin: 0; padding: 0; box-sizing: border-box; }
  html, body { width: 733px; height: 1200px; overflow: hidden; background: var(--paper); }
  .flyer { position: relative; width: 733px; height: 1200px; overflow: hidden;
    background: linear-gradient(135deg, var(--paper-shade) 0%, var(--white) 45%, var(--paper) 100%);
    font-family: "Open Sans", Arial, sans-serif; color: var(--white); }
  .flyer__shapes { position: absolute; inset: 0; }
  .flyer__block { position: absolute; }

  .headline { left: 26px; top: 44px; font-family: "Oswald", "Arial Narrow", sans-serif; font-weight: 600;
    color: var(--gold); font-size: 48px; line-height: 1.08; text-transform: uppercase; letter-spacing: 0.3px; }
  .subhead { left: 26px; top: 168px; width: 400px; font-family: "Roboto Condensed", Arial, sans-serif;
    color: var(--sky); font-size: 23px; line-height: 1.15; }
  .event-details { left: 26px; top: 258px; font-family: "Roboto Condensed", Arial, sans-serif;
    font-weight: 700; font-size: 21px; line-height: 1.32; }
  .section-title { font-family: "Roboto Condensed", Arial, sans-serif; font-weight: 700; color: var(--sky);
    font-size: 26px; margin-bottom: 6px; }
  .raffle { left: 26px; top: 376px; width: 380px; font-size: 14px; line-height: 1.38; }
  .note { font-size: 11px; line-height: 1.35; margin-top: 2px; }
  .prizes { left: 26px; top: 538px; width: 362px; font-size: 14px; line-height: 1.42; }
  .prizes ul { list-style: none; text-align: justify; }
  .prizes li { padding-left: 12px; text-indent: -12px; }
  .signups { left: 26px; top: 880px; width: 380px; font-size: 12px; line-height: 1.4; color: var(--gold); }
  .signups strong { font-weight: 600; }

  .photo { position: absolute; border: 3px solid var(--sky); }
  .photo--left { left: 26px; top: 1015px; width: 186px; height: 108px;
    background: linear-gradient(135deg, #7c6a5a, #c9b9a6 55%, #566a8c); }
  .photo--right { left: 228px; top: 1015px; width: 186px; height: 108px;
    background: linear-gradient(135deg, #6d8fb8, #d8c3a0 50%, #9c6f5a); }

  .choice { left: 440px; top: 618px; width: 280px; font-family: "Oswald", "Arial Narrow", sans-serif;
    font-weight: 500; color: var(--red); font-size: 32px; line-height: 1; text-transform: uppercase; }
  .choice__second { display: block; text-align: right; margin-top: 4px; }
  .drawings { left: 430px; top: 672px; width: 182px; color: var(--ink); font-size: 12.5px; line-height: 1.45; }
  .drawings .section-title { color: var(--label-blue); }
  .drawings .note { font-size: 10.5px; margin-top: 4px; }
  .food { right: 16px; top: 852px; width: 300px; text-align: right; color: var(--ink); font-size: 13.5px; line-height: 1.5; }
  .food .section-title { color: var(--label-blue); margin-bottom: 2px; }
  .food__items { margin-left: auto; width: 100px; }
  .food__basket { padding-left: 50px; }

  .brand { left: 452px; top: 1092px; display: flex; align-items: center; gap: 8px;
    font-family: "Roboto Condensed", Arial, sans-serif; font-weight: 700; color: var(--label-blue); font-size: 18px; }
  .brand__mark { width: 30px; height: 30px; border-radius: 50%; background: var(--label-blue); }
  .contact { left: 540px; top: 1072px; width: 185px; font-family: "Roboto Condensed", Arial, sans-serif; white-space: nowrap; }
  .contact__label { color: var(--label-blue); font-weight: 700; font-size: 14px; line-height: 1.15; }
  .contact__phone { color: var(--red); font-weight: 700; font-size: 29px; line-height: 1.15; }
</style>
</head>
<body>
<main class="flyer">
  <svg class="flyer__shapes" width="733" height="1200" viewBox="0 0 733 1200">
    <defs>
      <linearGradient id="panelFill" x1="0" y1="0" x2="1" y2="1">
        <stop offset="0" stop-color="#2a4ea6"/>
        <stop offset="1" stop-color="#1d3a8a"/>
      </linearGradient>
      <linearGradient id="crowdFill" x1="0" y1="0" x2="1" y2="1">
        <stop offset="0" stop-color="#6f7fa8"/>
        <stop offset="0.45" stop-color="#c7a58f"/>
        <stop offset="1" stop-color="#e9e2dc"/>
      </linearGradient>
    </defs>
    <polygon points="0,0 445,0 425,600 408,1200 0,1200" fill="url(#panelFill)"/>
    <g role="img" aria-label="Photo of smiling students and parents at a past celebration">
      <polygon points="445,0 733,0 733,612 425,600" fill="url(#crowdFill)"/>
    </g>
  </svg>

  <h1 class="flyer__block headline">Join the Brookmere<br>Learning Trust</h1>
  <p class="flyer__block subhead">as we celebrate BULD and its students, educational programs, and schools</p>

  <p class="flyer__block event-details">Thursday, March 26, 2015<br>5:00 p.m. – 8:00 p.m.<br>Brookmere Senior Academy</p>

  <section class="flyer__block raffle">
    <h2 class="section-title">Raffle Prizes</h2>
    <p>KORVAN 50" Class 1080p LED Smart HDTV<br>Zentra Prime Console w/ Motionbar<br>Donations of $2 each or 3 for $5, or 7 for $10</p>
    <p class="note">*Tickets are available at the BULD Administration Building/ Communications and at the schools. (You must be present to win.)</p>
  </section>

  <section class="flyer__block prizes">
    <h2 class="section-title">Prizes Galore!</h2>
    <ul>
      <li>• Campus with the highest percentage of adult attendance will win $300 + the Traveling</li>
      <li>• Trophy for one year.</li>
      <li>• Campus with the 2nd highest percentage of adult attendance will win $150.</li>
      <li>• Additional drawings for Teacher, Principal/ Asst. Principal, and District Personnel will be held.</li>
    </ul>
  </section>

  <section class="flyer__block signups">
    <p><strong>Students:</strong><br>Please sign up to be entered in a drawing for Pixora Mini.</p>
    <p><strong>Adults:</strong><br>Please sign up to be entered in a drawing for a $50 Shopwell Gift Card.</p>
  </section>

  <div class="photo photo--left" role="img" aria-label="Photo of a student using a microscope with a teacher"></div>
  <div class="photo photo--right" role="img" aria-label="Photo of families visiting school displays"></div>

  <h2 class="flyer__block choice">Your Choice<span class="choice__second">Your Prize</span></h2>

  <section class="flyer__block drawings">
    <h3 class="section-title">Drawings</h3>
    <p>7" Dravik NEBULA Pad 4<br>Fennix Streamlet<br>Brewlo Classic B20 Single Serve<br>External Hard Drive<br>Brewlo 3.0 B700 Coffee Brewing System w/ Carafe<br>Fennix Streamlet<br>Cotton Candy Maker</p>
    <p class="note">*For your donation of $1.00 per ticket, you may place your ticket(s) in one or all of the baskets. It's your choice. (You must be present to win.)</p>
  </section>

  <section class="flyer__block food">
    <h3 class="section-title">Food!</h3>
    <p class="food__items">Hot Dogs $1.00<br>Corn Dogs $0.75<br>Chips $0.50<br>Drinks $0.75<br>Cookies $0.75</p>
    <p class="food__basket">Baskets - $2.50 (Hot Dog or Corn Dog, Chips, Drink, Cookie)</p>
  </section>

  <div class="flyer__block brand"><span class="brand__mark"></span>BLT</div>
  <div class="flyer__block contact">
    <p class="contact__label">For more information<br>please call:</p>
    <p class="contact__phone">555-318-2946</p>
  </div>
</main>
</body>
</html>
```